Larder & Hearth - Premium Catering needs a new menu design.

I currently use menupro to make my own menus for printing and uploading to the website (PDF). I need a professional menu to replace my current menu. I wold like to mail these menus out so I'm thinking a tri-fold menu would be the best option. Similar to what pizzerias send out.

Need extra days to review

Logo Text

Would be good to reduce the text thickness of the letters "TIL" in the word TILMORE. Right now TIL has thicker text.

Colors

Designer to choose colors to be used in the design.

```html
<!DOCTYPE html>
<html lang="en">
<head>
<meta charset="utf-8">
<title>Tilmore – Larder &amp; Hearth – Menu</title>
<link rel="stylesheet" href="https://fonts.googleapis.com/css2?family=Arimo:wght@400;700&family=Crimson+Pro:ital,wght@0,400;0,700;1,400&family=Oswald:wght@600;700&display=swap">
<style>
:root{
  --bg:#13211a;
  --frame:#c65a22;
  --gold:#e6a23a;
  --olive:#a9a55b;
  --cream:#f1ece0;
  --white:#ffffff;
  --heading:#c9602a;
}
*{margin:0;padding:0;box-sizing:border-box}
html,body{width:927px;height:1200px;overflow:hidden;background:var(--bg)}
.menu{position:relative;width:927px;height:1200px;background:var(--bg);color:var(--cream);font-family:"Crimson Pro",Georgia,serif}
.menu *{position:absolute}
.menu .flow, .menu .flow *, .menu .inl{position:static}
.outer-line{left:7px;top:20px;width:913px;height:1160px;border:2px solid var(--gold);border-radius:6px}
.frame{left:25px;top:34px;width:877px;height:1130px;background:var(--frame)}
.panel{left:29px;top:39px;width:869px;height:1120px;background:var(--bg);border-radius:30px}
.info{font-family:Arimo,Arial,sans-serif;color:var(--gold);font-size:14px;line-height:20.5px;top:79px}
.hours{left:56px}
.contact{right:54px;text-align:right}
.logo-art{left:374px;top:49px;width:142px;height:68px}
.brand{left:0;width:927px;text-align:center;color:var(--white)}
.brand-name{top:112px;font-family:Oswald,Impact,sans-serif;font-weight:700;font-size:46px;letter-spacing:3px;line-height:56px}
.brand-sub{font-family:"Crimson Pro",Georgia,serif;font-weight:700;font-size:25px;letter-spacing:1px;line-height:26px}
.brand-sub.one{top:163px}
.brand-sub.two{top:190px}
.head{font-family:Oswald,Impact,sans-serif;font-weight:600;color:var(--heading);letter-spacing:3px;font-size:21px;line-height:24px;white-space:nowrap}
.note{color:var(--olive);font-size:12px;line-height:14px;text-align:center;white-space:nowrap}
.mi{display:flex;align-items:baseline;font-size:14.5px;line-height:18px;white-space:nowrap}
.mi .flow{display:flex}
.mi i{font-style:italic}
.lead{flex:1;border-bottom:2px dotted var(--cream);margin:0 5px;transform:translateY(-4px);position:static!important}
.price{font-family:Arimo,Arial,sans-serif;font-weight:700;font-size:13.5px;position:static!important}
.cont{font-size:14.5px;font-style:italic;line-height:18px;white-space:nowrap}
.bk{left:54px;width:392px}
.om{left:500px;width:391px}
.star{width:14px;height:14px;fill:var(--olive)}
.box{border:2px solid var(--olive);color:var(--olive);text-align:center;display:flex;flex-direction:column;justify-content:center}
.box span{position:static}
.lbl{font-size:9px;line-height:10px;color:var(--olive);text-align:center;transform:translateX(-50%)}
.row{font-size:14px;line-height:18px;white-space:nowrap}
.row i{font-style:italic}
.p{font-family:Arimo,Arial,sans-serif;font-weight:700;font-size:13px;line-height:18px;transform:translateX(-50%);white-space:nowrap}
.crow{font-size:12px;line-height:17px;font-style:italic;white-space:nowrap;letter-spacing:-0.1px}
.hot{font-family:Arimo,Arial,sans-serif;font-size:8px;font-style:normal;line-height:17px}
.veg{font-size:9px;font-style:italic;color:var(--olive);line-height:12px}
.foot{left:0;width:927px;top:1177px;text-align:center;color:var(--heading);font-size:14px}
</style>
</head>
<body>
<svg width="0" height="0" style="position:absolute">
  <symbol id="star" viewBox="0 0 24 24"><path d="M12 1.5l3.1 7 7.4.7-5.6 5 1.7 7.4L12 17.8 5.4 21.6l1.7-7.4-5.6-5 7.4-.7z"/></symbol>
</svg>
<main class="menu">
  <div class="outer-line"></div>
  <div class="frame"></div>
  <div class="panel"></div>

  <div class="info hours">OPEN DAILY AND MOST HOLIDAYS:<br>SUNDAY: 8AM - 5PM<br>MONDAY: 6AM - 5PM<br>TUESDAY-FRIDAY: 6AM - 7PM<br>SATURDAY: 7AM - 7PM</div>
  <div class="info contact">WWW.TILMOREDELI.COM<br>PHONE: 555 - 014 -2210<br>FAX: 555 - 014 -2427<br>12 ROUTE US -40<br>MARLOW SPRINGS, NJ 08999</div>

  <svg class="logo-art" role="img" aria-label="Illustration of a hoagie sandwich beneath a rising sun" viewBox="0 0 142 68">
    <defs><linearGradient id="artFill" x1="0" y1="0" x2="0" y2="1"><stop offset="0" stop-color="#d9b56a"/><stop offset="1" stop-color="#9b5a3a"/></linearGradient></defs>
    <rect x="0" y="0" width="142" height="68" rx="10" fill="url(#artFill)"/>
  </svg>

  <div class="brand brand-name">TILMORE</div>
  <div class="brand brand-sub one">LARDER &amp; HEARTH</div>
  <div class="brand brand-sub two">PREMIUM CATERING</div>

  <div class="head" style="left:0;width:895px;text-align:center;top:227px;font-size:20px">TILMORE’S FAMOUS HOAGIES</div>

  <!-- Breakfast -->
  <div class="head" style="left:93px;top:250px">BREAKFAST</div>
  <div class="note" style="left:110px;top:281px;font-size:13.5px">Served all day</div>
  <div class="head" style="left:86px;top:298px">SANDWICHES</div>

  <div class="mi bk" style="top:332px"><span class="flow">2 JUMBO EGGS</span><span class="lead"></span><span class="price">$2.59</span></div>
  <div class="mi bk" style="top:353px"><span class="flow">"&nbsp;&nbsp;WITH CHEESE</span><span class="lead"></span><span class="price">$3.09</span></div>
  <div class="mi bk" style="top:374px"><span class="flow">"&nbsp;&nbsp;WITH MEAT ~&nbsp;<i>Pork Roll, Sausage or Bacon</i></span><span class="lead"></span><span class="price">$4.09</span></div>
  <svg class="star" style="left:34px;top:394px"><use href="#star"/></svg>
  <div class="mi bk" style="top:395px"><span class="flow">"&nbsp;&nbsp;WITH MEAT AND CHEESE ~&nbsp;<i>Pork Roll, Sausage or</i></span><span class="lead"></span><span class="price">$4.59</span></div>
  <div class="cont" style="left:86px;top:413px">Bacon</div>

  <div class="mi bk" style="top:459px"><span class="flow">2&nbsp; EGGS ANY STYLE ~&nbsp;<i>served with home fries and toast</i></span><span class="lead"></span><span class="price">$5.99</span></div>
  <svg class="star" style="left:34px;top:479px"><use href="#star"/></svg>
  <div class="mi bk" style="top:480px"><span class="flow">2 EGGS ANY STYLE WITH MEAT ~&nbsp;<i>served with home fries</i></span><span class="lead"></span><span class="price">$7.99</span></div>
  <div class="cont" style="left:85px;top:498px">and toast</div>
  <div class="mi bk" style="top:518px"><span class="flow">FRENCH TOAST ~&nbsp;<i>made with homemade bread</i></span><span class="lead"></span><span class="price">$5.49</span></div>
  <div class="mi bk" style="top:539px"><span class="flow">FRENCH TOAST WITH MEAT</span><span class="lead"></span><span class="price">$7.49</span></div>
  <div class="mi bk" style="top:560px"><span class="flow">SHORT STACK OF PANCAKES (3)</span><span class="lead"></span><span class="price">$4.99</span></div>
  <div class="mi bk" style="top:581px"><span class="flow">SHORT STACK WITH MEAT</span><span class="lead"></span><span class="price">$6.99</span></div>

  <div class="box" style="left:64px;top:617px;width:214px;height:38px;font-size:11.5px;line-height:14px"><span>MEAT CHOICES:&nbsp; SAUSAGE, HAM</span><span>BACON, PORKROLL &amp; TURKEY BACON</span></div>

  <!-- Omelettes -->
  <div class="head" style="left:0;width:1464px;text-align:center;top:250px">OMELETTES</div>
  <div class="note" style="left:0;width:1456px;top:274px;font-size:11px;line-height:14px">MADE WITH 3 JUMBO EGGS<br>SERVED WITH HOME FRIES AND TOAST</div>
  <div class="mi om" style="top:305px"><span class="flow">CHEESE OMELETTE</span><span class="lead"></span><span class="price">$6.99</span></div>
  <svg class="star" style="left:479px;top:326px"><use href="#star"/></svg>
  <div class="mi om" style="top:326px"><span class="flow">BACON &amp; CHEESE OMELETTE</span><span class="lead"></span><span class="price">$7.99</span></div>
  <div class="mi om" style="top:347px"><span class="flow">BROCCOLI &amp; CHEESE OMELETTE</span><span class="lead"></span><span class="price">$7.99</span></div>
  <div class="mi om" style="top:368px"><span class="flow">MUSHROOM &amp; CHEESE OMELETTE</span><span class="lead"></span><span class="price">$7.99</span></div>
  <div class="mi om" style="top:389px"><span class="flow">WESTERN OMELETTE WITH CHEESE</span><span class="lead"></span><span class="price">$7.99</span></div>

  <div class="head" style="left:0;width:1428px;text-align:center;top:408px">BREAKFAST SPECIAL 2X4</div>
  <div class="note" style="left:0;width:1460px;top:433px;font-size:11px">SERVED WITH BUTTER AND SYRUP</div>
  <svg class="star" style="left:485px;top:452px"><use href="#star"/></svg>
  <div class="mi" style="left:504px;width:392px;top:452px"><span class="flow">2 PANCAKES, 2 EGGS, 2 SAUSAGE, AND 2 STRIPS OF .</span><span class="price" style="margin-left:8px">$8.99</span></div>
  <div class="cont" style="left:504px;top:470px;font-style:normal">BACON</div>

  <div class="box" style="left:593px;top:474px;width:208px;height:53px;font-size:11.5px;line-height:14.5px"><span>SIDE OF HOME FRIES&nbsp; $3.99</span><span>SIDE OF HASHBROWNS 2 PCS. $3.49</span><span>SIDE OF BREAKFAST MEAT&nbsp; $3.99</span></div>
  <div class="box" style="left:527px;top:543px;width:328px;height:37px;font-size:10.5px;line-height:13.5px"><span>HOAGIES MARKED AS "HOT" ARE TOASTED.</span><span>HOAGIES MARKED AS "SPICY" ARE MILD TO MEDIUM SPICY.</span></div>
  <div class="box" style="left:499px;top:596px;width:383px;height:56px;font-size:8.6px;line-height:11.6px;padding:0 5px"><span>PLEASE SPECIFY TOPPINGS:&nbsp; LETTUCE, TOMATO, ONION, SALT, PEPPER, OREGANO, OIL, VINEGAR, MAYO, MUSTARD, ETC.&nbsp; HOAGIES, SANDWICHES &amp; WRAPS THAT ARE MADE WITH CHEESE INCLUDE AMERICAN, PROVOLONE&nbsp; OR SWISS UNLESS OTHERWISE STATED.&nbsp; OTHER CHEESE SELECTIONS ARE ADDITIONAL.</span></div>

  <!-- The usual suspects -->
  <div class="head" style="left:53px;top:668px">THE USUAL SUSPECTS</div>
  <div class="lbl" style="left:313px;top:684px">REGULAR</div>
  <div class="lbl" style="left:369px;top:673px">JUMBO<br>HALF</div>
  <div class="lbl" style="left:428px;top:673px">JUMBO<br>WHOLE</div>

  <svg class="star" style="left:40px;top:695px"><use href="#star"/></svg>
  <div class="row" style="left:64px;top:696px">THE ITALIAN ~ <i>Ham, Capicola, Salami,</i></div>
  <div class="cont" style="left:92px;top:713px">Prosciutto &amp; Provolone Cheese</div>
  <div class="p" style="left:309px;top:696px">$7.09</div><div class="p" style="left:371px;top:696px">9.09</div><div class="p" style="left:426px;top:696px">17.99</div>

  <div class="row" style="left:61px;top:733px">THE AMERICAN ~ <i>Bologna, Cooked</i> .</div>
  <div class="cont" style="left:92px;top:751px">Salami, Ham &amp; American Cheese</div>
  <div class="p" style="left:309px;top:733px">$6.99</div><div class="p" style="left:371px;top:733px">8.99</div><div class="p" style="left:426px;top:733px">17.79</div>

  <div class="row" style="left:61px;top:771px">HAM ~ <i>choice of american, swiss or</i> .</div>
  <div class="cont" style="left:92px;top:789px">provolone</div>
  <div class="p" style="left:309px;top:771px">$6.99</div><div class="p" style="left:371px;top:771px">8.99</div><div class="p" style="left:426px;top:771px">17.79</div>

  <div class="row" style="left:61px;top:808px">CHICKEN SALAD ~ <i>choice of american,</i></div>
  <div class="cont" style="left:92px;top:826px">swiss or provolone</div>
  <div class="p" style="left:309px;top:808px">$7.49</div><div class="p" style="left:368px;top:808px">10.99</div><div class="p" style="left:426px;top:808px">21.79</div>

  <div class="row" style="left:61px;top:846px">TUNA SALAD ~ <i>choice of american,</i> .</div>
  <div class="cont" style="left:92px;top:864px">swiss or provolone</div>
  <div class="p" style="left:309px;top:846px">$7.49</div><div class="p" style="left:368px;top:846px">10.99</div><div class="p" style="left:426px;top:846px">21.79</div>

  <svg class="star" style="left:40px;top:882px"><use href="#star"/></svg>
  <div class="row" style="left:61px;top:883px">TURKEY ~ <i>choice of american, swiss or</i> .</div>
  <div class="cont" style="left:92px;top:901px">provolone</div>
  <div class="p" style="left:309px;top:883px">$7.99</div><div class="p" style="left:368px;top:883px">10.99</div><div class="p" style="left:426px;top:883px">21.79</div>

  <div class="row" style="left:61px;top:921px">ROASTBEEF ~ <i>choice of american, swiss</i> .</div>
  <div class="cont" style="left:92px;top:939px">or provolone</div>
  <div class="p" style="left:309px;top:921px">$8.49</div><div class="p" style="left:368px;top:921px">12.49</div><div class="p" style="left:426px;top:921px">24.79</div>

  <div class="row" style="left:61px;top:958px">THE OLD STYLE ~ <i>Dry Cured Hot</i> .</div>
  <div class="cont" style="left:92px;top:976px">Capicola, Prosciutto &amp; Sharp Provolone Cheese</div>
  <div class="p" style="left:309px;top:958px">$8.99</div><div class="p" style="left:368px;top:958px">12.99</div><div class="p" style="left:426px;top:958px">25.79</div>

  <svg class="star" style="left:40px;top:995px"><use href="#star"/></svg>
  <div class="row" style="left:61px;top:996px">SPICY OLD STYLE ~ <i>Hot Sopressata,</i> .</div>
  <div class="cont" style="left:92px;top:1014px">Dry Cured Hot Capicola, Sharp Provolone &amp; Sliced</div>
  <div class="cont" style="left:92px;top:1031px">Pepper Shooters.</div>
  <div class="p" style="left:309px;top:996px">$9.49</div><div class="p" style="left:368px;top:996px">13.49</div><div class="p" style="left:426px;top:996px">26.79</div>

  <svg class="star" style="left:40px;top:1050px"><use href="#star"/></svg>
  <div class="row" style="left:61px;top:1051px">TILMORE CHEESE STEAK ~ <i>piles of steak and</i></div>
  <div class="cont" style="left:92px;top:1069px">american cheese on our famous hoagie roll</div>
  <div class="p" style="left:363px;top:1051px">$11.99</div><div class="p" style="left:426px;top:1051px">23.79</div>

  <div class="row" style="left:61px;top:1089px">THE TILMORE ~ <i>Double Meat with Ham,</i> .</div>
  <div class="cont" style="left:92px;top:1106px">Salami, Bologna, Cooked Salami, Capicola, Pepperoni,</div>
  <div class="cont" style="left:92px;top:1123px">American, Swiss &amp; Provolone</div>
  <div class="p" style="left:363px;top:1089px">$12.99</div><div class="p" style="left:426px;top:1089px">25.79</div>

  <!-- Combination hoagies -->
  <div class="head" style="left:515px;top:668px">COMBINATION HOGIES</div>
  <div class="lbl" style="left:774px;top:683px">REGULAR</div>
  <div class="lbl" style="left:822px;top:673px">JUMBO<br>HALF</div>
  <div class="lbl" style="left:873px;top:673px">JUMBO<br>WHOLE</div>

  <div class="crow" style="left:553px;top:696px">1 ~ Turkey, Roast Beef, Ham &amp; Am. Chz. .</div>
  <div class="p" style="left:770px;top:695px">$7.59</div><div class="p" style="left:821px;top:695px">10.09</div><div class="p" style="left:872px;top:695px">19.99</div>

  <div class="crow" style="left:553px;top:713px">2 ~ Corned Beef or Pastrami, Swiss, .</div>
  <div class="crow" style="left:581px;top:728px">Coleslaw &amp; Russian dressing</div>
  <div class="p" style="left:770px;top:712px">$8.29</div><div class="p" style="left:821px;top:712px">11.29</div><div class="p" style="left:872px;top:712px">22.39</div>

  <div class="crow" style="left:553px;top:746px">3 ~ Roast Beef,&nbsp; Swiss, Coleslaw &amp; Russian .</div>
  <div class="crow" style="left:581px;top:762px">dressing</div>
  <div class="p" style="left:770px;top:745px">$8.99</div><div class="p" style="left:821px;top:745px">12.99</div><div class="p" style="left:872px;top:745px">25.79</div>

  <svg class="star" style="left:533px;top:779px"><use href="#star"/></svg>
  <div class="crow" style="left:553px;top:779px">4 ~ Turkey, Swiss, Coleslaw &amp; Russian&nbsp; .</div>
  <div class="crow" style="left:581px;top:795px">dressing</div>
  <div class="p" style="left:770px;top:778px">$8.49</div><div class="p" style="left:821px;top:778px">11.49</div><div class="p" style="left:872px;top:778px">22.79</div>

  <div class="crow" style="left:553px;top:812px">5 ~ Salsa Turkey, Montrey Jack Cheese .</div>
  <div class="crow" style="left:581px;top:827px">&amp;&nbsp; Chipotle Mayo</div>
  <div class="p" style="left:770px;top:811px">$7.99</div><div class="p" style="left:821px;top:811px">11.99</div><div class="p" style="left:872px;top:811px">23.79</div>

  <div class="crow" style="left:555px;top:845px">6 ~ BBQ Chicken, Bacon &amp; Cheddar&nbsp; .</div>
  <div class="p" style="left:770px;top:844px">$7.99</div><div class="p" style="left:821px;top:844px">11.99</div><div class="p" style="left:872px;top:844px">23.79</div>

  <svg class="star" style="left:519px;top:862px"><use href="#star"/></svg>
  <div class="crow" style="left:534px;top:862px"><span class="hot inl">HOT&nbsp;</span> 7 ~ Roast Pork, Sharp Provolone &amp;&nbsp; .</div>
  <div class="crow" style="left:581px;top:878px">Broccoli Rabe</div>
  <div class="p" style="left:770px;top:861px">$8.99</div><div class="p" style="left:821px;top:861px">12.99</div><div class="p" style="left:872px;top:861px">25.79</div>

  <div class="crow" style="left:555px;top:895px">8 ~ Prosciutto, Fresh Mozzarella &amp;&nbsp; .</div>
  <div class="crow" style="left:585px;top:913px">Roasted Pepper</div>
  <div class="p" style="left:770px;top:894px">$8.99</div><div class="p" style="left:821px;top:894px">12.99</div><div class="p" style="left:872px;top:894px">25.79</div>

  <div class="crow" style="left:555px;top:928px">9 ~ Honey Ham, Honey Turkey, Swiss &amp;&nbsp; .</div>
  <div class="crow" style="left:581px;top:943px">Honey Mustard</div>
  <div class="p" style="left:770px;top:927px">$7.99</div><div class="p" style="left:821px;top:927px">11.99</div><div class="p" style="left:872px;top:927px">23.79</div>

  <svg class="star" style="left:519px;top:961px"><use href="#star"/></svg>
  <div class="crow" style="left:534px;top:961px"><span class="hot inl">HOT&nbsp;</span> 10 ~ Chicken Cutlet dipped in Buffalo&nbsp; .</div>
  <div class="crow" style="left:581px;top:976px">sauce and our very own&nbsp; Bleu Cheese Dressing</div>
  <div class="p" style="left:770px;top:960px">$7.99</div><div class="p" style="left:821px;top:960px">11.49</div><div class="p" style="left:872px;top:960px">22.79</div>

  <div class="crow" style="left:534px;top:994px"><span class="hot inl">HOT&nbsp;</span> 11 ~ Chicken Cutlet, Sharp Provolone&nbsp; .</div>
  <div class="crow" style="left:581px;top:1009px">topped with Fresh Broccoli Rabe</div>
  <div class="p" style="left:770px;top:993px">$8.99</div><div class="p" style="left:821px;top:993px">12.49</div><div class="p" style="left:872px;top:993px">24.79</div>

  <div class="crow" style="left:532px;top:1027px"><span class="hot inl">HOT&nbsp;</span> 12 ~ Chicken Cutlet, Pepper Jack &amp;&nbsp; .</div>
  <div class="crow" style="left:581px;top:1042px">Chipotle Mayo</div>
  <div class="p" style="left:770px;top:1026px">$7.99</div><div class="p" style="left:821px;top:1026px">11.49</div><div class="p" style="left:872px;top:1026px">22.79</div>

  <svg class="star" style="left:519px;top:1060px"><use href="#star"/></svg>
  <div class="crow" style="left:532px;top:1060px"><span class="hot inl">HOT&nbsp;</span> 13 ~ Chicken Cutlet, Fresh Mozzarella,&nbsp; .</div>
  <div class="crow" style="left:581px;top:1075px">Roasted Pepper &amp; Balsamic Vinaigrette</div>
  <div class="p" style="left:770px;top:1059px">$8.99</div><div class="p" style="left:821px;top:1059px">12.49</div><div class="p" style="left:872px;top:1059px">24.79</div>

  <div class="crow" style="left:532px;top:1093px"><span class="hot inl">HOT&nbsp;</span> 14 ~ Chicken Cutlet, Honey Ham, Swiss &amp;</div>
  <div class="crow" style="left:581px;top:1108px">Honey Mustard</div>
  <div class="p" style="left:770px;top:1092px">$8.49</div><div class="p" style="left:821px;top:1092px">11.99</div><div class="p" style="left:872px;top:1092px">23.79</div>

  <div class="veg" style="left:524px;top:1122px">Veggie</div>
  <svg style="left:526px;top:1132px;width:24px;height:6px" viewBox="0 0 24 6"><path d="M0 3h20M17 0.5l4 2.5-4 2.5" stroke="#a9a55b" stroke-width="1.2" fill="none"/></svg>
  <div class="crow" style="left:553px;top:1126px">15 ~ 3 Cheese -American, Prov.&nbsp; &amp; Swiss&nbsp; .</div>
  <div class="p" style="left:770px;top:1125px">$6.99</div><div class="p" style="left:824px;top:1125px">9.99</div><div class="p" style="left:872px;top:1125px">19.79</div>

  <div class="foot">*all prices subject to change without notice*</div>
</main>
</body>
</html>
```